Flyer Design

we are cleaning company specialize in home cleaning, based in North Shore in Auckland (NZ).
Company name RW is initial of bright wren.
we provide professional, high standard,attention to detail service,
to make dust-free, sparkling house and no-stress family.

(business practice)--don't write this title
"colour coded cleaning system"
---we use different colour's microfiber cloths and mop heads for more hygene.
"green and clean"
---we use eco-friendly, non-toxic cleaning products for environment and your family's health.

service we offer
regular cleaning service
--weekly, fortnightly, monthly
one-off cleaning service
---move in/out cleaning
---rental inspection cleaning
---spring cleaning
---open home cleaning
---remodeling clean-up
---special occasion cleaning(event,party)

special cleaning
---window cleaning
---oven cleaning
---house washing(water blasting)

Free in home no obligation consultation and 50% off first service.
contact no; Rob and Helen 021 0487 5620,09-561-2047
e-mail info@rwcleaning.example.nz
www.rwcleaning.example.nz

we would like to see designs that use colours blue and lite pink, clean, bright and friendly image.

Target Market(s)

Woman aged between late 30th to 60th, housewives, career woman, senior etc.

Industry/Entity Type

Environment

Requirements
Should not have
• For the introduction instead of writing what I have written above verbatim, would you be able to go to our website and paraphrase/reword the introduction that's already there?

Also please don't use the picture on the website, we are planning to change the picture. Thanks.

```html
<!DOCTYPE html>
<html lang="en">
<head>
<meta charset="utf-8">
<title>RW Cleaning Services – Flyer</title>
<link rel="stylesheet" href="https://fonts.googleapis.com/css2?family=Barlow:wght@400;500&family=Barlow+Condensed:wght@500;600&family=Mulish:wght@500;600;700;800&display=swap">
<style>
  :root {
    --page-bg: #f8f7f3;
    --sheet: #ffffff;
    --brand-blue: #1a67b8;
    --deep-blue: #0d4f96;
    --ink: #111111;
    --ink-soft: #2e2e2e;
    --pink-band: #f9d3e6;
    --sky-panel: #93d4f5;
    --photo-light: #f4f6f8;
    --photo-warm: #f3c76a;
    --photo-cool: #a9cbe8;
  }
  * { margin: 0; padding: 0; box-sizing: border-box; }
  html, body { width: 1200px; height: 1000px; overflow: hidden; background: var(--page-bg); }
  .flyer {
    position: absolute; left: 279px; top: 51px; width: 632px; height: 893px;
    background: var(--sheet); overflow: hidden;
  }
  .brand { position: absolute; left: 44px; top: 30px; width: 180px; text-align: center;
    font-family: "Barlow Condensed", sans-serif; }
  .brand-initials { display: block; font-size: 76px; line-height: 70px; font-weight: 500; letter-spacing: 3px; color: var(--brand-blue); }
  .brand-name { display: block; font-size: 26px; line-height: 30px; margin-top: 2px; font-weight: 600; color: var(--ink-soft); }
  .contact { position: absolute; left: 43px; top: 157px; font-family: "Barlow", sans-serif; color: var(--ink-soft); }
  .contact-call { font-size: 20px; font-weight: 500; color: var(--ink); letter-spacing: .6px; line-height: 24px; }
  .contact-line { font-size: 15px; line-height: 19px; letter-spacing: .3px; }
  .offer { position: absolute; left: 354px; top: 58px; width: 260px; text-align: center;
    font-family: "Mulish", sans-serif; color: var(--brand-blue); font-weight: 600; }
  .offer-line { font-size: 16.5px; line-height: 24px; }
  .offer-big { font-size: 29px; font-weight: 800; }
  .offer-mid { font-size: 19px; font-weight: 600; }
  .stamp { position: absolute; left: 500px; top: 188px; }
  .photo { position: absolute; left: 0; top: 284px; width: 632px; height: 262px;
    background: radial-gradient(ellipse at 50% 90%, var(--photo-warm) 0%, rgba(243,199,106,0) 38%),
                linear-gradient(180deg, var(--photo-light) 0%, var(--photo-cool) 70%, var(--photo-light) 100%); }
  .pink-band { position: absolute; left: 0; top: 546px; width: 632px; height: 14px; background: var(--pink-band); }
  .info { position: absolute; left: 0; top: 560px; width: 632px; height: 333px; background: var(--sky-panel);
    padding: 16px 26px 0; font-family: "Mulish", sans-serif; color: var(--brand-blue); }
  .intro { text-align: center; font-weight: 600; font-size: 16.5px; line-height: 23px;
    text-transform: uppercase; letter-spacing: .3px; }
  .practices { display: flex; gap: 16px; margin-top: 12px; }
  .practice { flex: 1; background: rgba(255,255,255,.55); border-left: 4px solid var(--pink-band); padding: 7px 10px; }
  .block-title { font-size: 14px; line-height: 18px; font-weight: 800; color: var(--deep-blue); text-transform: uppercase; }
  .practice p, .service-list li { font-size: 12.5px; line-height: 16px; font-weight: 500; color: var(--deep-blue); }
  .services-heading { margin-top: 11px; text-align: center; font-size: 15px; font-weight: 800; color: var(--deep-blue);
    text-transform: uppercase; letter-spacing: 1px; }
  .services { display: flex; gap: 14px; margin-top: 5px; }
  .service { flex: 1; }
  .service-wide { flex: 1.5; }
  .service-list { list-style: none; margin-top: 3px; }
  .service-list li::before { content: "•"; margin-right: 5px; color: var(--brand-blue); }
  .service-wide .service-list { columns: 2; column-gap: 10px; }
</style>
</head>
<body>
  <main class="flyer">
    <div class="brand">
      <span class="brand-initials">RW</span>
      <span class="brand-name">Cleaning Services</span>
    </div>

    <div class="contact">
      <p class="contact-call">CALL US NOW!</p>
      <p class="contact-line">Rob &amp; Helen</p>
      <p class="contact-line">021 0487 5620, 09-561-2047</p>
      <p class="contact-line">e-mail info@rwcleaning.example.nz</p>
      <p class="contact-line">www.rwcleaning.example.nz</p>
    </div>

    <div class="offer">
      <p class="offer-line"><span class="offer-big">FREE</span> In home</p>
      <p class="offer-line">no obligation consultation</p>
      <p class="offer-line">&amp; <span class="offer-big">50% OFF</span></p>
      <p class="offer-line offer-mid">FIRST SERVICE.</p>
    </div>

    <svg class="stamp" width="92" height="92" viewBox="0 0 92 92" aria-hidden="true">
      <circle cx="46" cy="46" r="43" fill="none" stroke="#1a67b8" stroke-width="3"/>
      <circle cx="46" cy="46" r="30" fill="none" stroke="#1a67b8" stroke-width="1.5"/>
    </svg>

    <div class="photo" role="img" aria-label="Three smiling cleaners in aprons and uniforms holding mops and a bucket of cleaning supplies, with yellow mop buckets at the sides"></div>

    <div class="pink-band"></div>

    <section class="info">
      <p class="intro">
        Careful, professional home cleaning that notices every detail —<br>
        so you come home to a spotless, dust-free house<br>
        and a relaxed, happy family.
      </p>

      <div class="practices">
        <div class="practice">
          <h3 class="block-title">Colour coded cleaning system</h3>
          <p>Separate colours of microfibre cloths and mop heads for better hygiene.</p>
        </div>
        <div class="practice">
          <h3 class="block-title">Green and clean</h3>
          <p>Eco-friendly, non-toxic products, kind to the planet and your family's health.</p>
        </div>
      </div>

      <h2 class="services-heading">Services we offer</h2>
      <div class="services">
        <div class="service">
          <h3 class="block-title">Regular cleaning</h3>
          <ul class="service-list">
            <li>Weekly</li>
            <li>Fortnightly</li>
            <li>Monthly</li>
          </ul>
        </div>
        <div class="service service-wide">
          <h3 class="block-title">One-off cleaning</h3>
          <ul class="service-list">
            <li>Move in / out</li>
            <li>Rental inspection</li>
            <li>Spring cleaning</li>
            <li>Open home</li>
            <li>Remodeling clean-up</li>
            <li>Events &amp; parties</li>
          </ul>
        </div>
        <div class="service">
          <h3 class="block-title">Special cleaning</h3>
          <ul class="service-list">
            <li>Window cleaning</li>
            <li>Oven cleaning</li>
            <li>House washing</li>
          </ul>
        </div>
      </div>
    </section>
  </main>
</body>
</html>
```